Cedar Grove Steward Book Cover and Back Design

DESIGN BRIEF: The Cedar Grove Steward Book Cover
Author: Mayor Bernard T. Hale
Title: The Cedar Grove Steward
Subtitle: Raising Builders that shape neighbourhoods
Genre: Leadership / Personal Development / Public Service
Format: Paperback + eBook + Hardcover
Design a visually compelling, iconic book cover that captures the essence of authentic, legacy-driven leadership using the metaphor of the mango tree. The cover should be vibrant, symbolic, and memorable—something that could stand alone as a brand and invite both credibility and curiosity.
Cover should NOT include:
Author’s face or personal photo
Overly busy visuals or political imagery
Literal images of mayors, buildings, or people
Cover SHOULD include:
A single iconic mango tree or mango fruit with visible deep roots
A vibrant and rich color palette—think mango orange, deep green, warm gold, and earth tones
A design that feels both modern and timeless, with symbolic depth
A sense of growth, depth, and legacy
Room for bold typography that pops in print and thumbnails
🖼️ VISUAL CONCEPT IDEAS
(Designer may interpret creatively, but these are preferred themes.)
A stylized mango tree with glowing mangoes and roots extending downward, set against a vibrant background (sunrise or rich green sky)
A mango fruit icon with leaves and roots subtly worked into the shape — could be used across brand platforms
Optional: Split background showing transformation — one side dry/cracked earth, the other lush and fruitful
Clean, modern layout with breathing space and balance between image and title
✍️ TYPOGRAPHY
Title Font: Strong, elegant serif or modern classic (e.g., Playfair Display, Garamond, or Libre Baskerville)
Subtitle Font: Clean and crisp sans serif (e.g., Lato, Montserrat)
Author Name: Bold, uppercase — not oversized, but clearly legible
🔠 COPY FOR COVER
Title:
The Cedar Grove Steward
Subtitle:
Raising Builders That Shape Neighbourhoods
Author Name:
Mayor Bernard T. Hale
Optional Tagline or Teaser (for back or spine):
Stop performing like a politician. Start producing like a leader.
🔧 FORMAT DELIVERABLES
Front cover (paperback and hardcover versions)
Spine and back cover layout (with placeholder for barcode and description)
Web-optimized version for Borvix PDP and other retailers
Square version for social media promotion
Optional: Icon version of tree or mango for branding
Back of book: Are you tired of leadership that looks impressive but produces no lasting fruit?
In a culture obsessed with image over integrity, quick wins over deep roots, and self-promotion over public service, we need a new kind of leader—one who leads for legacy, not likes.
What if you stopped leading like an apple tree—and started leading like a mango tree?
Apple trees grow fast and look good for a season, but their shallow roots can’t weather the storms. Mango trees grow slowly, but they last for generations—producing sweet, lasting fruit long after their planter is gone.
This isn’t just a metaphor. It’s a mindset shift. And it’s the key to leadership that actually transforms people, places, and policy.
Mayor Bernard Hale has spent over a decade turning Dumfries, Virginia, from a town people drove through into a town people now drive to. Under his leadership:
• A former landfill became a half-billion-dollar resort
• A forgotten town rediscovered its purpose• A generation of young people began to see public service as purpose, not performance
In The Cedar Grove Steward, you’ll discover how to:
✅ Lead from your authentic strengths—not trends or titles✅ Identify the unique problem you were born to solve✅ Build coalitions rooted in trust, not transaction✅ Make decisions that create sustainable change✅ Develop future leaders who multiply your impact✅ Leave a legacy that grows long after you’re gone
Whether you’re an elected official, aspiring public servant, nonprofit founder, or community-builder, this book will help you lead like a tree: planted deeply, growing steadily, and bearing fruit that feeds others for generations.
Stop performing like a politician. Start producing like a leader.Plant deep. Lead strong. Leave fruit that lasts.
By the time you finish this book, you won’t just understand the mango tree model—you’ll own it. You’ll walk away with clarity, courage, and a roadmap to become the kind of leader your community needs and your future demands.
Leadership

```html
<!DOCTYPE html>
<html lang="en">
<head>
<meta charset="utf-8">
<title>The Cedar Grove Steward — Front Cover</title>
<link rel="stylesheet" href="https://fonts.googleapis.com/css2?family=Bebas+Neue&family=Oswald:wght@400;700&family=Playfair+Display:ital,wght@1,600&display=swap">
<style>
  :root {
    --backdrop: #e9e7e4;
    --paper: #ffffff;
    --ink: #0d0d0d;
    --mango: #e0901a;
    --leaf-light: #4f9a3a;
    --leaf-deep: #1f4a32;
  }
  html, body {
    margin: 0;
    width: 1200px;
    height: 1200px;
    overflow: hidden;
    background: var(--backdrop);
  }
  .stage {
    width: 1200px;
    height: 1200px;
    display: flex;
    align-items: center;
    justify-content: center;
  }
  .book-cover {
    width: 761px;
    height: 1140px;
    display: block;
    background: var(--paper);
  }
  .title-article {
    font-family: "Playfair Display", Georgia, serif;
    font-style: italic;
    font-weight: 600;
    fill: var(--ink);
  }
  .title-rule { fill: var(--ink); }
  .title-main {
    font-family: "Bebas Neue", "Oswald", sans-serif;
    fill: var(--mango);
  }
  .title-second {
    font-family: "Bebas Neue", "Oswald", sans-serif;
    fill: var(--ink);
  }
  .subtitle {
    font-family: "Oswald", "Arial Narrow", sans-serif;
    font-weight: 400;
    fill: var(--mango);
  }
  .author {
    font-family: "Oswald", "Arial Narrow", sans-serif;
    font-weight: 700;
    fill: var(--ink);
  }
</style>
</head>
<body>
<main class="stage">
  <svg class="book-cover" viewBox="0 0 883 1322" xmlns="http://www.w3.org/2000/svg" aria-labelledby="cover-title">
    <title id="cover-title">The Cedar Grove Steward by Mayor Bernard T. Hale</title>
    <defs>
      <radialGradient id="tree-tone" cx="50%" cy="42%" r="60%">
        <stop offset="0%" stop-color="var(--leaf-light)"/>
        <stop offset="100%" stop-color="var(--leaf-deep)"/>
      </radialGradient>
    </defs>

    <rect class="cover-paper" x="0" y="0" width="883" height="1322" fill="var(--paper)"/>

    <!-- Title header -->
    <polygon class="title-rule" points="60,92 333,88 333,98"/>
    <polygon class="title-rule" points="824,92 549,88 549,98"/>
    <text class="title-article" x="441" y="124" font-size="100" text-anchor="middle">The</text>

    <text class="title-main" x="60" y="396" font-size="363" textLength="760" lengthAdjust="spacingAndGlyphs">CEDAR</text>
    <text class="title-second" x="60" y="552" font-size="197" textLength="764" lengthAdjust="spacingAndGlyphs">GROVE STEWARD</text>

    <text class="subtitle" x="60" y="664" font-size="93" textLength="764" lengthAdjust="spacingAndGlyphs">RAISING BUILDERS THAT</text>
    <text class="subtitle" x="119" y="756" font-size="93" textLength="645" lengthAdjust="spacingAndGlyphs">SHAPE NEIGHBOURHOODS</text>

    <!-- Cover artwork area -->
    <g class="cover-artwork" role="img" aria-label="Illustration of a leafy fruit tree laden with golden fruit, standing on a ground line between two shrubs">
      <rect x="178" y="782" width="518" height="452" rx="40" fill="url(#tree-tone)"/>
    </g>

    <text class="author" x="156" y="1302" font-size="50" textLength="588" lengthAdjust="spacing">MAYOR BERNARD T. HALE</text>
  </svg>
</main>
</body>
</html>
```